Modern labels for Tidlock products

We need a new design of our labels for the product “Tidlock” (https://www.tidlock.eu/#) . The reason why we want to change our labels is to get a modern and more advanced look of our product. We also want to create a unique product that is attractive for our customers, even if the product are used in hospitals and healthcare centers for collecting dangerous waste.

There is three sizes of labels (55x95, 90x95, 170x95 mm) for different boxes, but the label will contain similar information. There are certain requirements and factors from regulations/standards that you need to follow when you create the new layout. But it’s up to you to change the design. You can work with background, fonts, effects, colors, structure, pattern, new symbols, logotype etc. The label could be any color, but the container will stay yellow so they have to look good together.

Keywords: Elegant, modern, functional, attractive, exclusive

Target Market(s)

Hospitals and healthcare centers

Industry/Entity Type

Product

Font styles to use
Serif
Sans Serif

Colors

Designer to choose colors to be used in the design.

Requirements
Must have
• Requirements for the regulations ADR UN3291 and ISO 23907 (PDF).
• * Symbol for danger waste
• * Filling level
• * "Danger"
• * Symbol for no second use
• * Symbol for manufaturer
• * Referencenumber
• * Text "”Clinical waste, Unspecified, N.O.S.”"
• * Area for series, certification, size and useful capacity
• * Area for Illustrations.
• * Text “Autoclavable at 134 c”, “Do not force closure” and “Do not overfill”.
• * Text for certification ”UN 3291 1H2/Y0,3/S/YR/N/KVP4817B”
• Three different sizes (55x95, 90x95, 170x95).
• More info in PDF "3kravspecifikation"
Nice to have
• A modern, elegant, advanced look of our label.
Should not have
• The information must be clear and readable, not too decorative/handwriting fonts.

```html
<!DOCTYPE html>
<html lang="en">
<head>
<meta charset="utf-8">
<title>Tidlock – clinical waste labels</title>
<link rel="stylesheet" href="https://fonts.googleapis.com/css2?family=Roboto+Condensed:wght@400;700&family=Roboto:wght@300;400;500;700&display=swap">
<style>
  :root{
    --yellow:#fde01f;
    --teal-1:#12a49c;
    --teal-2:#1cc9c2;
    --teal-dark:#0d564d;
    --white:#ffffff;
    --label-text:#d8f4f1;
    --danger:#e0232a;
    --ink:#1b1b1b;
    --panel-line:#2d2d2d;
    --art:#e4ecec;
  }
  *{box-sizing:border-box;margin:0;padding:0}
  html,body{width:1003px;height:1200px;overflow:hidden}
  body{background:var(--yellow);position:relative;font-family:"Roboto",sans-serif;color:var(--white)}
  .label{position:absolute;overflow:hidden;background:linear-gradient(115deg,var(--teal-1) 0%,var(--teal-2) 55%,var(--teal-1) 100%)}
  .abs{position:absolute}

  .fill-level{position:absolute;display:flex;align-items:center;gap:14px;left:0;right:0}
  .fill-level .line{flex:1;height:1.5px;background:var(--white);position:relative}
  .fill-level .line.left::before,.fill-level .line.right::after{content:"";position:absolute;top:-6px;width:12px;height:12px;border-bottom:1.5px solid var(--white)}
  .fill-level .line.left::before{left:1px;border-left:1.5px solid var(--white);transform:rotate(45deg)}
  .fill-level .line.right::after{right:1px;border-right:1.5px solid var(--white);transform:rotate(-45deg)}
  .fill-level .word{letter-spacing:.5em;font-weight:400;white-space:nowrap}

  .title{font-family:"Roboto Condensed",sans-serif;font-weight:700;text-transform:uppercase;color:var(--white)}
  .un-box{position:absolute;background:var(--teal-dark);border-radius:4px;text-align:center;font-family:"Roboto Condensed",sans-serif;display:flex;flex-direction:column;justify-content:center}
  .un-box .un{font-weight:700;line-height:.95;display:block;letter-spacing:-.01em}
  .un-box .code{display:block;font-weight:400;white-space:nowrap;line-height:1.15}
  .danger{font-family:"Roboto Condensed",sans-serif;font-weight:700;color:var(--danger);line-height:1;letter-spacing:.01em}
  .ref{font-family:"Roboto",sans-serif;font-weight:300;white-space:nowrap}
  .maker .name{font-family:"Roboto",sans-serif;font-weight:700;line-height:1;display:flex;align-items:center;gap:5px}
  .maker .name .mark{display:inline-block;background:var(--white)}
  .maker .detail{font-family:"Roboto Condensed",sans-serif;display:block;line-height:1.3}

  .field-label{position:absolute;text-align:center;text-transform:uppercase;letter-spacing:.5em;color:var(--label-text);font-weight:400}
  .field-box{position:absolute;background:var(--white);border-radius:4px}
  .info-band{position:absolute;background:var(--teal-dark);color:var(--white)}
  .info-band b{font-weight:500}
</style>
</head>
<body>

<!-- 170 x 95 label -->
<section class="label label-large" style="left:116px;top:174px;width:786px;height:437px">
  <div class="fill-level" style="top:35px;padding:0 24px">
    <span class="line left"></span><span class="word" style="font-size:18px">FILLING LEVEL</span><span class="line right"></span>
  </div>

  <svg class="abs hazard-diamond" style="left:20px;top:53px" width="152" height="152" viewBox="0 0 100 100">
    <polygon points="50,1 99,50 50,99 1,50" fill="var(--white)"/>
    <polygon points="50,5 95,50 50,95 5,50" fill="none" stroke="var(--ink)" stroke-width="1.6"/>
    <circle cx="50" cy="36" r="12" fill="var(--art)" role="img" aria-label="Biohazard symbol"/>
    <text x="50" y="82" text-anchor="middle" font-family="Roboto, sans-serif" font-size="10" fill="var(--ink)">6</text>
  </svg>

  <div class="un-box" style="left:14px;top:218px;width:176px;height:66px">
    <span class="un" style="font-size:52px">UN3291</span>
    <span class="code" style="font-size:12px">&#9417; 1H2/Y0.3/S/YR/N/KVP4817B</span>
  </div>

  <div class="abs danger" style="left:14px;top:302px;font-size:28px">DANGER</div>
  <div class="abs ref" style="left:14px;top:338px;font-size:12px">XXXXX-XX-XX-XX</div>

  <div class="abs maker" style="left:128px;top:302px">
    <span class="name" style="font-size:25px"><span class="mark" style="width:9px;height:9px"></span>Tidlock</span>
    <span class="detail" style="font-size:11px;margin-left:27px">Norrvik, Sweden<br>www.tidlock.eu</span>
  </div>

  <svg class="abs no-reuse" style="left:270px;top:298px" width="56" height="56" viewBox="0 0 56 56">
    <circle cx="28" cy="28" r="27" fill="var(--teal-dark)"/>
    <circle cx="28" cy="28" r="21" fill="none" stroke="var(--white)" stroke-width="2.5"/>
    <text x="28" y="37" text-anchor="middle" font-family="Roboto, sans-serif" font-weight="500" font-size="26" fill="none" stroke="var(--white)" stroke-width="1.4">2</text>
    <line x1="14" y1="42" x2="42" y2="14" stroke="var(--white)" stroke-width="2.2"/>
  </svg>

  <svg class="abs instructions" style="left:206px;top:58px" width="260" height="224" viewBox="0 0 260 224" role="img" aria-label="Assembly and closing instructions in three steps">
    <rect x="0" y="0" width="260" height="224" rx="5" fill="var(--white)"/>
    <rect x="12" y="10" width="100" height="78" fill="var(--art)"/>
    <rect x="128" y="10" width="122" height="78" fill="var(--art)"/>
    <rect x="12" y="104" width="100" height="110" fill="var(--art)"/>
    <rect x="128" y="104" width="122" height="110" fill="var(--art)"/>
    <line x1="117" y1="0" x2="117" y2="224" stroke="var(--panel-line)" stroke-width="1.5"/>
    <line x1="0" y1="93" x2="260" y2="93" stroke="var(--panel-line)" stroke-width="1.5"/>
    <text x="4" y="26" font-family="Roboto, sans-serif" font-size="13" fill="var(--ink)">1</text>
    <text x="120" y="26" font-family="Roboto, sans-serif" font-size="13" fill="var(--ink)">3</text>
    <text x="4" y="124" font-family="Roboto, sans-serif" font-size="13" fill="var(--ink)">2</text>
  </svg>

  <div class="abs title" style="left:476px;top:56px;font-size:40px;line-height:37px">Clinical waste,<br>unspecified,<br>N.O.S.</div>

  <div class="field-label" style="left:484px;width:286px;top:175px;font-size:10.5px">Place / Clinic</div>
  <div class="field-box" style="left:484px;top:188px;width:286px;height:40px"></div>
  <div class="field-label" style="left:484px;width:286px;top:234px;font-size:10.5px">Department</div>
  <div class="field-box" style="left:484px;top:247px;width:286px;height:40px"></div>
  <div class="field-label" style="left:484px;width:286px;top:293px;font-size:10.5px">Sealed by &amp; date</div>
  <div class="field-box" style="left:484px;top:306px;width:286px;height:40px"></div>

  <div class="info-band" style="left:0;top:362px;width:786px;height:64px;font-size:16px;font-weight:300;line-height:23px">
    <div class="abs" style="right:616px;top:9px;text-align:right;white-space:nowrap">Do not overfill<br>Do not force closure</div>
    <div class="abs" style="left:200px;top:9px;white-space:nowrap">Autoclavable at<br><b>134 °C</b></div>
    <div class="abs" style="right:205px;top:9px;text-align:right;white-space:nowrap">Series: <b>Orbit</b><br>Certification: <b>ISO23907:2012</b></div>
    <div class="abs" style="left:602px;top:9px;white-space:nowrap">Size: <b>2,2 L</b><br>Useful capacity: <b>1,76 L</b></div>
  </div>
</section>

<!-- 90 x 95 label -->
<section class="label label-medium" style="left:116px;top:646px;width:439px;height:416px">
  <div class="fill-level" style="top:26px;padding:0 18px">
    <span class="line left"></span><span class="word" style="font-size:16px">FILLING LEVEL</span><span class="line right"></span>
  </div>

  <div class="abs title" style="right:228px;top:62px;font-size:29px;line-height:26px;text-align:right">Clinical waste,<br>unspecified,<br>N.O.S.</div>

  <svg class="abs hazard-diamond" style="left:9px;top:121px" width="90" height="90" viewBox="0 0 100 100">
    <polygon points="50,1 99,50 50,99 1,50" fill="var(--white)"/>
    <polygon points="50,5 95,50 50,95 5,50" fill="none" stroke="var(--ink)" stroke-width="1.6"/>
    <circle cx="50" cy="36" r="12" fill="var(--art)" role="img" aria-label="Biohazard symbol"/>
    <text x="50" y="82" text-anchor="middle" font-family="Roboto, sans-serif" font-size="10" fill="var(--ink)">6</text>
  </svg>

  <svg class="abs no-reuse" style="left:170px;top:154px" width="40" height="40" viewBox="0 0 56 56">
    <circle cx="28" cy="28" r="27" fill="var(--teal-dark)"/>
    <circle cx="28" cy="28" r="21" fill="none" stroke="var(--white)" stroke-width="2.5"/>
    <text x="28" y="37" text-anchor="middle" font-family="Roboto, sans-serif" font-weight="500" font-size="26" fill="none" stroke="var(--white)" stroke-width="1.4">2</text>
    <line x1="14" y1="42" x2="42" y2="14" stroke="var(--white)" stroke-width="2.2"/>
  </svg>

  <svg class="abs instructions" style="left:223px;top:60px" width="208" height="180" viewBox="0 0 260 224" role="img" aria-label="Assembly and closing instructions in three steps">
    <rect x="0" y="0" width="260" height="224" rx="5" fill="var(--white)"/>
    <rect x="14" y="10" width="98" height="78" fill="var(--art)"/>
    <rect x="130" y="10" width="120" height="78" fill="var(--art)"/>
    <rect x="14" y="104" width="98" height="110" fill="var(--art)"/>
    <rect x="130" y="104" width="120" height="110" fill="var(--art)"/>
    <line x1="117" y1="0" x2="117" y2="224" stroke="var(--panel-line)" stroke-width="1.5"/>
    <line x1="0" y1="93" x2="260" y2="93" stroke="var(--panel-line)" stroke-width="1.5"/>
    <text x="3" y="28" font-family="Roboto, sans-serif" font-size="15" fill="var(--ink)">1</text>
    <text x="120" y="28" font-family="Roboto, sans-serif" font-size="15" fill="var(--ink)">3</text>
    <text x="3" y="126" font-family="Roboto, sans-serif" font-size="15" fill="var(--ink)">2</text>
  </svg>

  <div class="un-box" style="left:12px;top:218px;width:166px;height:60px">
    <span class="un" style="font-size:45px">UN3291</span>
    <span class="code" style="font-size:11px">&#9417; 1H2/Y0.3/S/YR/N/KVP4817B</span>
  </div>

  <div class="abs maker" style="left:8px;top:291px">
    <span class="name" style="font-size:20px"><span class="mark" style="width:8px;height:8px"></span>Tidlock</span>
    <span class="detail" style="font-size:9px;margin-left:20px">Norrvik, Sweden<br>www.tidlock.eu</span>
  </div>
  <div class="abs danger" style="left:110px;top:295px;font-size:22px">DANGER</div>
  <div class="abs ref" style="left:107px;top:321px;font-size:10px">XXXXX-XX-XX-XX</div>

  <div class="info-band" style="left:6px;top:343px;width:172px;height:58px;border-radius:3px;font-size:8px;font-weight:300;line-height:11px">
    <div class="abs" style="left:4px;top:5px;white-space:nowrap">Size: <b>2,2 L</b><br>Useful capacity: <b>1,76 L</b></div>
    <div class="abs" style="right:4px;top:5px;text-align:right;white-space:nowrap">Do not overfill<br>Do not force closure</div>
    <div class="abs" style="left:4px;top:34px;white-space:nowrap">Series: <b>Orbit</b><br>Cert.: <b>ISO23907:2012</b></div>
    <div class="abs" style="right:4px;top:34px;text-align:right;white-space:nowrap">Autoclavable at<br><b>134 °C</b></div>
  </div>

  <div class="field-label" style="left:190px;width:238px;top:257px;font-size:9px">Place / Clinic</div>
  <div class="field-box" style="left:190px;top:270px;width:238px;height:32px"></div>
  <div class="field-label" style="left:190px;width:238px;top:306px;font-size:9px">Department</div>
  <div class="field-box" style="left:190px;top:318px;width:238px;height:32px"></div>
  <div class="field-label" style="left:190px;width:238px;top:355px;font-size:9px">Sealed by &amp; date</div>
  <div class="field-box" style="left:190px;top:367px;width:238px;height:32px"></div>
</section>

<!-- 55 x 95 label -->
<section class="label label-small" style="left:647px;top:646px;width:255px;height:440px">
  <div class="fill-level" style="top:16px;padding:0 10px;gap:8px">
    <span class="line left"></span><span class="word" style="font-size:10px">FILLING LEVEL</span><span class="line right"></span>
  </div>

  <svg class="abs instructions" style="left:15px;top:34px" width="187" height="161" viewBox="0 0 260 224" role="img" aria-label="Assembly and closing instructions in three steps">
    <rect x="0" y="0" width="260" height="224" rx="5" fill="var(--white)"/>
    <rect x="14" y="10" width="98" height="78" fill="var(--art)"/>
    <rect x="130" y="10" width="120" height="78" fill="var(--art)"/>
    <rect x="14" y="104" width="98" height="110" fill="var(--art)"/>
    <rect x="130" y="104" width="120" height="110" fill="var(--art)"/>
    <line x1="117" y1="0" x2="117" y2="224" stroke="var(--panel-line)" stroke-width="1.5"/>
    <line x1="0" y1="93" x2="260" y2="93" stroke="var(--panel-line)" stroke-width="1.5"/>
    <text x="3" y="28" font-family="Roboto, sans-serif" font-size="16" fill="var(--ink)">1</text>
    <text x="120" y="28" font-family="Roboto, sans-serif" font-size="16" fill="var(--ink)">3</text>
    <text x="3" y="126" font-family="Roboto, sans-serif" font-size="16" fill="var(--ink)">2</text>
  </svg>

  <div class="info-band" style="left:211px;top:34px;width:34px;height:396px;border-radius:3px">
    <div class="abs" style="width:396px;height:34px;left:-181px;top:181px;transform:rotate(-90deg);font-size:8px;font-weight:300;line-height:10px">
      <div class="abs" style="left:8px;top:7px;white-space:nowrap">Do not overfill<br>Do not force closure</div>
      <div class="abs" style="left:90px;top:7px;white-space:nowrap">Autoclavable at<br><b>134 °C</b></div>
      <div class="abs" style="right:8px;top:7px;white-space:nowrap">Series: <b>Orbit</b>&nbsp;&nbsp;Size: <b>2,2 L</b><br>Certification: <b>ISO23907:2012</b>&nbsp;&nbsp;Useful capacity: <b>1,76 L</b></div>
    </div>
  </div>

  <div class="abs title" style="right:56px;top:202px;font-size:18px;line-height:17px;text-align:right">Clinical waste,<br>unspecified,<br>N.O.S.</div>

  <svg class="abs hazard-diamond" style="left:11px;top:198px" width="60" height="60" viewBox="0 0 100 100">
    <polygon points="50,1 99,50 50,99 1,50" fill="var(--white)"/>
    <polygon points="50,5 95,50 50,95 5,50" fill="none" stroke="var(--ink)" stroke-width="1.8"/>
    <circle cx="50" cy="36" r="12" fill="var(--art)" role="img" aria-label="Biohazard symbol"/>
    <text x="50" y="82" text-anchor="middle" font-family="Roboto, sans-serif" font-size="11" fill="var(--ink)">6</text>
  </svg>

  <svg class="abs no-reuse" style="left:67px;top:240px" width="28" height="28" viewBox="0 0 56 56">
    <circle cx="28" cy="28" r="27" fill="var(--teal-dark)"/>
    <circle cx="28" cy="28" r="21" fill="none" stroke="var(--white)" stroke-width="3"/>
    <text x="28" y="37" text-anchor="middle" font-family="Roboto, sans-serif" font-weight="500" font-size="26" fill="none" stroke="var(--white)" stroke-width="1.6">2</text>
    <line x1="14" y1="42" x2="42" y2="14" stroke="var(--white)" stroke-width="2.6"/>
  </svg>

  <div class="abs danger" style="left:14px;top:261px;font-size:15px">DANGER</div>
  <div class="abs ref" style="left:14px;top:278px;font-size:6px">XXXXX-XX-XX-XX</div>

  <div class="abs maker" style="left:13px;top:287px">
    <span class="name" style="font-size:14px"><span class="mark" style="width:6px;height:6px"></span>Tidlock</span>
    <span class="detail" style="font-size:6px;margin-left:14px">Norrvik, Sweden<br>www.tidlock.eu</span>
  </div>

  <div class="un-box" style="left:93px;top:272px;width:109px;height:43px">
    <span class="un" style="font-size:31px">UN3291</span>
    <span class="code" style="font-size:7.5px">&#9417; 1H2/Y0.3/S/YR/N/KVP4817B</span>
  </div>

  <div class="field-label" style="left:12px;width:191px;top:322px;font-size:6px">Place / Clinic</div>
  <div class="field-box" style="left:12px;top:330px;width:191px;height:25px;border-radius:3px"></div>
  <div class="field-label" style="left:12px;width:191px;top:359px;font-size:6px">Department</div>
  <div class="field-box" style="left:12px;top:366px;width:191px;height:26px;border-radius:3px"></div>
  <div class="field-label" style="left:12px;width:191px;top:395px;font-size:6px">Sealed by &amp; date</div>
  <div class="field-box" style="left:12px;top:402px;width:191px;height:26px;border-radius:3px"></div>
</section>

</body>
</html>
```